Coaching and Tutoring that removes all obstacles and leads to success and happiness

Tutoring maths giving confidence, clarity and success to students of all abilities. Tutoring from 14 years to 18 years old. Dealing with exam preparation and stress.
Coaching confidence, resilience and ultimately happiness and freedom.
The design to inspire and reassure people of a safe pair of hands as well excitement of the beginning of something new in their lives.

Target Market(s)

20 -30 year olds

Industry/Entity Type

Self Development and Education

Contact Information for Business Card

Confidence Coach and Maths Tutor

Font styles to use
Sans Serif

Colors
EE7325
F08F49
F5BC92
FAE3D3
FDF4ED

Requirements
Must have
• Success and Happiness

```html
<!DOCTYPE html>
<html lang="en">
<head>
<meta charset="utf-8">
<title>Bright &amp; Steady – Business Card</title>
<link rel="stylesheet" href="https://fonts.googleapis.com/css2?family=Montserrat:wght@700;800&family=Roboto:wght@400;500;700&display=swap">
<style>
  :root {
    --backdrop: #2a2a2a;
    --orange: #ee7325;
    --orange-light: #f08f49;
    --orange-deep: #d8621b;
    --peach: #f5bc92;
    --blush: #fae3d3;
    --cream: #fdf4ed;
    --ink: #333333;
    --charcoal: #3a3a3a;
    --white: #ffffff;
  }
  * { box-sizing: border-box; margin: 0; padding: 0; }
  html, body { width: 1200px; height: 1138px; overflow: hidden; background: var(--backdrop); }
  .canvas { position: relative; width: 1200px; height: 1138px; }

  .card { position: absolute; border-radius: 16px; overflow: hidden; }

  /* Front */
  .card-front {
    left: 274px; top: 186px; width: 623px; height: 376px;
    background: linear-gradient(135deg, var(--orange-light) 0%, var(--orange) 50%, var(--orange-deep) 100%);
    color: var(--white); text-align: center;
  }
  .front-name {
    position: absolute; left: 0; right: 0; top: 126px;
    font-family: "Montserrat", sans-serif; font-weight: 800; font-size: 55px;
    letter-spacing: -0.5px; color: var(--white); white-space: nowrap;
  }
  .front-tagline {
    position: absolute; left: 0; right: 0; top: 196px;
    font-family: "Montserrat", sans-serif; font-weight: 800; font-size: 16px;
    letter-spacing: 19px; padding-left: 19px; color: var(--cream); white-space: nowrap;
  }
  .front-web {
    position: absolute; left: 0; right: 0; top: 328px;
    font-family: "Roboto", sans-serif; font-size: 16px; letter-spacing: 5px;
    padding-left: 5px; color: var(--cream); white-space: nowrap;
  }

  /* Back */
  .card-back {
    left: 276px; top: 608px; width: 618px; height: 374px;
    background: linear-gradient(180deg, var(--cream) 0%, #fbeee4 60%, var(--blush) 100%);
    color: var(--ink); font-family: "Roboto", sans-serif;
  }
  .brand-dot {
    position: absolute; left: 56px; top: 64px; width: 56px; height: 56px;
    border-radius: 50%; background: var(--orange);
  }
  .brand-name {
    position: absolute; left: 166px; top: 54px;
    font-family: "Montserrat", sans-serif; font-weight: 800; font-size: 40px;
    color: var(--orange); letter-spacing: -0.5px; white-space: nowrap;
  }
  .brand-tagline {
    position: absolute; left: 168px; top: 103px;
    font-family: "Montserrat", sans-serif; font-weight: 800; font-size: 12px;
    letter-spacing: 13.6px; color: var(--ink); white-space: nowrap;
  }
  .person { position: absolute; left: 35px; top: 208px; }
  .person-name { font-weight: 700; font-size: 23px; color: var(--orange); line-height: 28px; }
  .person-role { font-size: 16.5px; line-height: 22px; }
  .address { position: absolute; left: 36px; top: 292px; font-size: 16.5px; line-height: 23px; }
  .contacts { position: absolute; left: 334px; top: 228px; list-style: none; font-size: 16.5px; }
  .contacts li { display: flex; align-items: center; height: 23.5px; white-space: nowrap; }
  .contacts svg { width: 16px; height: 14px; margin-right: 8px; fill: var(--orange); }
  .bands { position: absolute; left: 0; bottom: 0; width: 618px; height: 48px; }
  .footer-line {
    position: absolute; left: 290px; right: 0; bottom: 11px; text-align: center;
    font-size: 16.5px; color: var(--white); white-space: nowrap;
  }
</style>
</head>
<body>
<main class="canvas">

  <section class="card card-front" aria-label="Card front">
    <h1 class="front-name">Bright &amp; Steady</h1>
    <p class="front-tagline">COACH AND TUTOR</p>
    <p class="front-web">www.brightsteady.com</p>
  </section>

  <section class="card card-back" aria-label="Card back">
    <span class="brand-dot"></span>
    <h2 class="brand-name">Bright &amp; Steady</h2>
    <p class="brand-tagline">COACH AND TUTOR</p>

    <div class="person">
      <p class="person-name">John Doe Smith</p>
      <p class="person-role">Managing Director</p>
    </div>

    <p class="address">17 Meadow Row, Fairford,<br>Brookvale, US 204518</p>

    <ul class="contacts">
      <li>
        <svg viewBox="0 0 16 14" aria-hidden="true"><path d="M1 4c0-2 3-3 7-3s7 1 7 3v1h-3.5V3.5h-7V5H1z"/><path d="M3 6h10l1.5 7h-13z"/><circle cx="8" cy="9.5" r="2" fill="#fdf4ed"/></svg>
        555-014-2290
      </li>
      <li>
        <svg viewBox="0 0 16 14" aria-hidden="true"><path d="M1 2h14v10H1z"/><path d="M1.5 2.5 8 8l6.5-5.5M1.5 11.5l5-4.5M14.5 11.5l-5-4.5" stroke="#fdf4ed" stroke-width="1.2" fill="none"/></svg>
        john@brightsteady.com
      </li>
      <li>
        <svg viewBox="0 0 16 14" aria-hidden="true"><circle cx="8" cy="7" r="6.5"/><path d="M1.5 7h13M8 0.5v13M3 3.5h10M3 10.5h10" stroke="#fdf4ed" stroke-width="1" fill="none"/><ellipse cx="8" cy="7" rx="3" ry="6.5" stroke="#fdf4ed" stroke-width="1" fill="none"/></svg>
        www.brightsteady.com
      </li>
    </ul>

    <svg class="bands" viewBox="0 0 618 48" preserveAspectRatio="none" aria-hidden="true">
      <rect x="0" y="33" width="618" height="15" fill="var(--charcoal)"/>
      <path d="M290 0H618V48H266Z" fill="var(--orange)"/>
    </svg>
    <p class="footer-line">Coaching confidence, resilience</p>
  </section>

</main>
</body>
</html>
```